Small Accounting Practice needs something creative

We need a business card design for a new small accounting practice based in Perth, Australia. The name of the practice is 'Kowra Ledger Partners Pty Ltd'. We providing Tax, Bookkeeping and Accounting services. Our target are individuals and small businesses. We want the design to be simply and creative. Also, we can the design can help us to gain people's trust.

Target Market(s)

Individuals and small businesses.

Industry/Entity Type

Accounting

Colors

Designer to choose colors to be used in the design.

```html
<!DOCTYPE html>
<html lang="en">
<head>
<meta charset="utf-8">
<title>Kowra Ledger Partners – Business Card</title>
<link rel="stylesheet" href="https://fonts.googleapis.com/css2?family=Roboto+Slab:wght@600&family=Questrial&family=Oswald:wght@600&display=swap">
<style>
  :root {
    --backdrop: #87898b;
    --card-light: #e4e6e9;
    --card-light-edge: #d9dbdf;
    --band: #eef0f2;
    --ink: #1d1d1f;
    --ink-soft: #333438;
    --rule: #2a2a2c;
    --card-dark: #000000;
    --on-dark: #ffffff;
  }
  * { margin: 0; padding: 0; box-sizing: border-box; }
  html, body { width: 1200px; height: 1000px; overflow: hidden; }
  body { background: var(--backdrop); position: relative; }

  .card { position: absolute; width: 731px; height: 395px; }

  .card-front {
    left: 207px; top: 75px;
    background: linear-gradient(180deg, var(--card-light) 0%, var(--card-light-edge) 100%);
  }
  .card-front .band {
    position: absolute; left: 0; right: 0; background: var(--band); opacity: .7;
  }
  .band-top { top: 75px; height: 48px; }
  .band-bottom { top: 287px; height: 43px; }
  .card-front .rules { position: absolute; inset: 0; }

  .role {
    position: absolute; left: 0; width: 740px; top: 84px; text-align: center;
    font: 600 22px/1 "Roboto Slab", serif; color: var(--ink); letter-spacing: .2px;
  }
  .person {
    position: absolute; left: 0; width: 743px; top: 165px; text-align: center;
    font: 400 42px/1 "Questrial", sans-serif; color: var(--ink); letter-spacing: 1px;
  }
  .credential {
    position: absolute; left: 0; width: 743px; top: 213px; text-align: center;
    font: 400 23px/1 "Questrial", sans-serif; color: var(--ink-soft); letter-spacing: 1px;
  }
  .email {
    position: absolute; left: 0; width: 743px; top: 298px; text-align: center;
    font: 400 19px/1 "Questrial", sans-serif; color: var(--ink-soft);
  }

  .card-back {
    left: 266px; top: 515px; background: var(--card-dark);
    display: flex; align-items: center; justify-content: center;
  }
  .company-name {
    font: 600 42px/1 "Oswald", sans-serif; color: var(--on-dark);
    letter-spacing: -.5px; margin-top: -6px;
  }
</style>
</head>
<body>
  <section class="card card-front" aria-label="Card front">
    <div class="band band-top"></div>
    <div class="band band-bottom"></div>
    <svg class="rules" width="731" height="395" viewBox="0 0 731 395" aria-hidden="true">
      <line x1="80" y1="0" x2="80" y2="392" stroke="var(--rule)" stroke-width="2"/>
      <line x1="88" y1="20" x2="88" y2="390" stroke="var(--rule)" stroke-width="1"/>
      <line x1="0" y1="342" x2="731" y2="342" stroke="var(--rule)" stroke-width="2"/>
      <line x1="10" y1="349" x2="725" y2="349" stroke="var(--rule)" stroke-width="1"/>
    </svg>
    <p class="role">Accountant &amp; Small Business Consultant</p>
    <h1 class="person">Owen Tarrant</h1>
    <p class="credential">Registered ASIC Agent 48107</p>
    <p class="email">Email: owen@kowraledger.com.au</p>
  </section>

  <section class="card card-back" aria-label="Card back">
    <h2 class="company-name">Kowra Ledger Partners Pty Ltd</h2>
  </section>
</body>
</html>
```